Home and interior page website design for HVAC company - Velmor Corp.

Create homepage and one interior page website design for an HVAC (Heating and AC) company. Current website is: https://velmorcorp.example/.

Client has specifically asked that the new site look inviting, informative and interactive. They mentioned that the logo on a white background doesn't look appealing and would like to see other options. (I have included the white background one from their current website as well as the one on an image that the client sent me) The site must include their financing widget (we have the code for this) in a prominent place. Image can be found here: https://getlendquick.example/badges/lendquick-financing.png.

The content from their existing site belongs to the company that built their site and have said we cannot use any of it. This development site (http://velmorwebd.qrbdev.example/) is what we originally created from our template for them before they decided they wanted a custom built site. The content there is what will need to be on the new home page.

We have gathered images from the client that they would like used throughout the site in this folder: https://climbrisk-my.filebox.example/:f:/g/personal/officelogin_climbrisk_filebox_example/Xq2m-R7TpLoWnZbYuCdE5FgHjK8NvA3sQwErTyUiOpLk?e=7KPZRT. They would like the photos used to be in tune with the topic being spoken about so if the topic is maintenance on a central AC system the photo used to lead that topic should be of a unit being cleaned.

For the testimonials section please also include a button or "Click here for more testimonials" as requested by the client.

Top Level NAV should include: Home, Residential, Commercial, Testimonials, Gallery, About Us, Coupons, Contact Us

For the interior page, we're looking for the same inviting, informative and interactive feel to the site, preferably with a banner of some sort and the form close to the top of the page if not able to keep it above the fold in the banner. Page should also include sections with clients images used to avoid a wall of text.

Example Websites that the client likes:
https://www.brelkordairworks.example/
https://www.quellitemp.example/?ref=PzR8vLm2KqT4nW9sXe6YuJ3aBc
https://www.torvandclimate.example/nny/
https://www.wexlo.example/
https://otterbrookheat.example/

Industry/Entity Type

Hvac

Number of Pages Required

2 page

Requirements
Must have
• *Summarized from project description:
-financing image in prominent place
-content from development site
-images from clients folder
-button or "click here.." note in testimonials section
-form above the fold
Nice to have
-logo not on white background

```html
<!DOCTYPE html>
<html lang="en">
<head>
<meta charset="utf-8">
<title>Velmor Mechanical Contractors – HVAC Services</title>
<link href="https://fonts.googleapis.com/css2?family=Roboto:wght@400;500;700&display=swap" rel="stylesheet">
<style>
:root{
  --blue:#1e73be;
  --blue-light:#6aa6dc;
  --orange:#ff8c00;
  --ink:#222;
  --muted:#777;
  --grey-bg:#f2f2f2;
  --band:#3b4366;
  --footer:#2f3654;
  --white:#fff;
}
*{margin:0;padding:0;box-sizing:border-box}
html,body{width:1200px;height:2844px;overflow:hidden;background:var(--white)}
body{font-family:"Roboto",Arial,sans-serif;color:var(--ink)}
.page{position:relative;width:1200px;height:2844px;overflow:hidden}
.abs{position:absolute}
.btn{position:absolute;display:flex;align-items:center;justify-content:center;border-radius:20px;font-size:9.5px;font-weight:500;text-transform:uppercase;letter-spacing:.3px}
.btn-orange{background:var(--orange);color:var(--white)}
.btn-blue{background:var(--blue);color:var(--white)}
.btn-outline-white{border:1.5px solid var(--white);color:var(--white)}
.btn-outline-blue{border:1.5px solid var(--blue);color:var(--blue);background:var(--white)}
.eyebrow{font-size:8.5px;font-weight:700;letter-spacing:1.6px;color:var(--blue);text-transform:uppercase}

/* header */
.site-header{position:absolute;left:0;top:0;width:1200px;height:55px;background:var(--white)}
.brand{left:173px;top:8px;display:flex;align-items:center;gap:8px;font-size:26px;font-weight:700;color:#111}
.brand-dot{width:18px;height:18px;border-radius:50%;background:#111}
.emergency{left:628px;top:17px;font-size:13px;color:#333}
.emergency b{font-size:18px;color:var(--blue);font-weight:700;margin-left:4px}
.main-nav{position:absolute;left:0;top:55px;width:1200px;height:37px;background:var(--blue)}
.main-nav a{position:absolute;top:0;height:37px;display:flex;align-items:center;color:var(--white);font-size:9.5px;font-weight:500;text-decoration:none}
.main-nav a.active{background:var(--orange);left:162px;width:63px;justify-content:center}

/* hero */
.hero{position:absolute;left:0;top:92px;width:1200px;height:380px;background:linear-gradient(110deg,#2a3446 0%,#161c27 55%,#222b3b 100%)}
.hero h1{position:absolute;left:162px;top:103px;font-size:31px;font-weight:500;line-height:42px;color:var(--white);letter-spacing:.2px}
.hero h1 .accent{color:var(--blue);font-weight:700}
.hero .lede{left:162px;top:230px;font-size:12px;color:var(--white)}
.quote-form{position:absolute;left:767px;top:53px;width:271px;height:327px;background:var(--white)}
.quote-form h2{position:absolute;left:0;width:271px;top:20px;text-align:center;font-size:16px;font-weight:500;color:#111}
.field{position:absolute;left:18px;width:235px;height:32px;border:1px solid #aaa;font-size:8px;color:#333;display:flex;align-items:center;padding-left:20px}
.field::before{content:"";position:absolute;left:8px;width:6px;height:6px;background:#666;border-radius:50%}
.field.area{height:60px;align-items:flex-start;padding-top:8px}
.field.area::before{top:10px}

/* about */
.about{position:absolute;left:0;top:472px;width:1200px;height:472px;background:var(--blue);clip-path:polygon(0 0,100% 0,100% 406px,0 472px)}
.about-frame{left:162px;top:70px;width:335px;height:267px;border:3px solid var(--blue-light)}
.about-photo{left:175px;top:61px;width:354px;height:264px;background:linear-gradient(135deg,#c7d6e6,#6d8ba8 60%,#3e5670)}
.about .eyebrow{position:absolute;left:599px;top:67px;color:#d7e6f5}
.about h2{position:absolute;left:599px;top:82px;font-size:25px;font-weight:500;color:var(--white)}
.about p{position:absolute;left:599px;top:133px;width:333px;font-size:10px;line-height:17.5px;color:var(--white)}

/* services */
.services{position:absolute;left:0;top:878px;width:1200px;height:566px;background:var(--grey-bg);z-index:-1}
.section-title{position:absolute;left:0;width:1200px;text-align:center}
.section-title h2{font-size:24px;font-weight:500;color:#222;margin-top:6px}
.section-title .rule{width:60px;height:2px;background:var(--orange);margin:14px auto 0}
.service-card{position:absolute;top:1093px;width:204px;height:285px;background:var(--white);box-shadow:0 1px 4px rgba(0,0,0,.08);text-align:center}
.service-icon{width:70px;height:70px;border-radius:50%;background:#eee;margin:14px auto 0;display:flex;align-items:center;justify-content:center}
.service-card h3{font-size:15px;font-weight:500;margin-top:16px;color:#222}
.service-card p{font-size:10px;line-height:16.3px;color:var(--muted);width:182px;margin:12px auto 0}
.service-card .btn{left:40px;top:238px;width:124px;height:28px}

/* why */
.why-item{position:absolute;width:230px}
.why-item h3{font-size:14.5px;font-weight:500;color:#222;white-space:nowrap}
.why-item p{font-size:9.8px;line-height:16px;color:var(--muted);margin-top:5px;width:186px}
.why-left{left:179px;text-align:right}
.why-left p{margin-left:auto}
.why-right{left:807px}

/* financing */
.financing{position:absolute;left:0;top:1982px;width:1200px;height:125px;background:var(--blue)}
.fin-brand{left:325px;top:28px;display:flex;align-items:center;gap:6px;font-size:24px;font-weight:500;color:var(--orange)}
.fin-brand span.dot{width:14px;height:14px;border-radius:50%;background:var(--orange)}
.financing .divider{left:506px;top:27px;width:1px;height:78px;background:rgba(255,255,255,.35)}
.financing h2{position:absolute;left:533px;top:38px;font-size:21px;font-weight:400;line-height:26px;color:var(--white)}

/* testimonials */
.testimonials h2{position:absolute;left:188px;top:2186px;font-size:25px;font-weight:500;color:#222}
.t-divider{left:425px;top:2164px;width:1px;height:100px;background:#ddd}
.t-stars{left:447px;top:2165px;font-size:9px;color:#333;display:flex;gap:10px;align-items:center}
.t-stars i{font-style:normal;color:var(--orange);letter-spacing:-1px;font-size:10px}
.t-text{left:447px;top:2183px;width:550px;font-size:9px;line-height:16.5px;color:#666}
.t-client{left:447px;top:2243px;display:flex;align-items:center;gap:10px;font-size:13px;color:var(--blue)}
.t-client .avatar{width:18px;height:18px;border-radius:50%;background:#ddd}

/* help */
.help-title{left:188px;top:2340px;font-size:24px;font-weight:700;color:var(--orange)}
.help-call{left:452px;top:2343px;font-size:14.5px;font-weight:500;color:#222}
.help-call b{font-size:22px;color:var(--blue);font-weight:700;margin-left:4px;vertical-align:-2px}

/* connect */
.connect{position:absolute;left:0;top:2390px;width:1200px;height:88px;background:var(--band)}
.connect h2{position:absolute;left:263px;top:20px;font-size:19px;font-weight:500;color:var(--white)}
.connect p{position:absolute;left:266px;top:46px;font-size:9.5px;font-weight:500;color:var(--white)}
.signup{left:614px;top:31px;width:265px;height:28px;background:var(--white);font-size:9.5px;color:#777;display:flex;align-items:center;padding-left:34px}
.signup::before{content:"";position:absolute;left:12px;top:10px;width:14px;height:9px;border:1px solid #999}
.signup-btn{left:879px;top:31px;width:59px;height:28px;background:var(--blue);color:var(--white);font-size:9px;display:flex;align-items:center;justify-content:center}

/* footer */
.site-footer{position:absolute;left:0;top:2478px;width:1200px;height:366px;background:var(--footer);color:#dfe3ee}
.site-footer h2{position:absolute;left:160px;top:40px;font-size:19px;font-weight:500;color:var(--white)}
.f-rule{position:absolute;left:162px;width:876px;height:1px;background:#56607f}
.f-col{position:absolute;top:94px;font-size:8.5px;line-height:17.6px;text-transform:uppercase}
.f-col h4{font-size:8.5px;font-weight:400;color:var(--blue-light);letter-spacing:.4px;margin-bottom:8px}
.f-col .current{color:var(--orange)}
.f-col .sub{text-transform:none;padding-left:10px}
.f-col table{border-collapse:collapse}
.f-col td{padding:0 18px 0 0;font-size:8.5px;line-height:17.6px}
.f-loc{text-transform:none;font-size:10px}
.f-loc .lbl{color:var(--blue-light)}
.pay{position:absolute;width:25px;height:15px;border-radius:2px}
.social{position:absolute;width:19px;height:19px;border-radius:50%;top:2710px}
.copyright{left:0;width:1200px;top:2818px;text-align:center;font-size:8.5px;color:#cfd4e2}
.copyright span{color:var(--blue-light)}
</style>
</head>
<body>
<div class="page">

  <header class="site-header">
    <div class="abs brand"><span class="brand-dot"></span>Velmor Corp.</div>
    <div class="abs emergency">Emergency Services <b>(718) 555-0147</b></div>
    <div class="btn btn-orange" style="left:921px;top:14px;width:117px;height:26px;font-size:8.5px;font-weight:700">Get an Appoinment</div>
  </header>
  <nav class="main-nav">
    <a class="active">HOME</a>
    <a style="left:248px">RESIDENTIAL</a>
    <a style="left:350px">COMMERCIAL</a>
    <a style="left:455px">TESTIMONIALS</a>
    <a style="left:564px">GALLERY</a>
    <a style="left:646px">ABOUT US</a>
    <a style="left:734px">COUPONS</a>
    <a style="left:821px">CONTACT US</a>
  </nav>

  <section class="hero" role="img" aria-label="Background photo of ceiling ductwork and HVAC equipment in a commercial building">
    <h1>COMMERCIAL &amp; RESIDENTIAL<br><span class="accent">HVAC INSTALLATION, MAINTAINESS</span><br>&amp; AC REPAIR SERVICES</h1>
    <div class="abs lede">Great Costumer Service And Even Better Prices</div>
    <div class="btn btn-blue" style="left:162px;top:270px;width:110px;height:26px">Contact Us</div>
    <form class="quote-form">
      <h2>SCHEDULE SERVICE NOW</h2>
      <div class="field" style="top:59px">Enter Your Name</div>
      <div class="field" style="top:104px">Enter Your Email</div>
      <div class="field" style="top:149px">Enter Your Phone</div>
      <div class="field area" style="top:196px">How Can We Help</div>
      <div class="btn btn-outline-blue" style="left:75px;top:275px;width:123px;height:24px;font-size:8.5px">Submit Inquery</div>
    </form>
  </section>

  <section class="about">
    <div class="abs about-frame"></div>
    <div class="abs about-photo" role="img" aria-label="Photo of a technician in a hard hat servicing an outdoor AC condenser unit with gauges"></div>
    <div class="eyebrow">Our History</div>
    <h2>About Our Company</h2>
    <p>Established in June 2008 by Marco Delgado in the Bronx. Velmor Mechanical Contractors CORP. prides tself in being able to establish great working relationships with it's customers. Ensuring nothing less then a flawless installation, great craftsmanship and over all excellent customer service. Velmor Mechanical Contractors CORP. specializes in water cooled systems, heat pumps, Air Conditioning systems, roof top packaged units, High efficiency Heating equipment, Solar Hot water systems, Refrigeration equipment, oil fired equipment. We work diligently with our partners to insure every projects success</p>
    <div class="btn btn-outline-white" style="left:599px;top:307px;width:122px;height:26px">Read More</div>
    <div class="btn btn-orange" style="left:731px;top:307px;width:122px;height:26px">Meet Our Team</div>
  </section>

  <div class="services"></div>
  <div class="section-title" style="top:1004px">
    <div class="eyebrow">Our Best Services</div>
    <h2>Company Services</h2>
    <div class="rule"></div>
  </div>

  <article class="service-card" style="left:163px">
    <div class="service-icon"><svg width="30" height="34" viewBox="0 0 30 34" fill="none" stroke="#1e73be" stroke-width="2"><path d="M15 2c2 7 10 11 10 20a10 10 0 0 1-20 0c0-5 3-8 5-11 1 4 3 5 5 5-2-5-1-10 0-14z"/><circle cx="15" cy="25" r="3" fill="#ff8c00" stroke="none"/></svg></div>
    <h3>Heating</h3>
    <p>In publishing and graphic design, Lorem ipsum is a placeholder text commonly used to demonstrate the visual form of a document or a typeface without Lorem ipsum may be used as a before final copy is available.</p>
    <div class="btn btn-orange">Read More</div>
  </article>
  <article class="service-card" style="left:386px">
    <div class="service-icon"><svg width="36" height="36" viewBox="0 0 36 36" fill="none" stroke="#ff8c00" stroke-width="1.8"><circle cx="18" cy="18" r="15"/><circle cx="18" cy="18" r="3" stroke="#1e73be"/><path d="M18 15c-2-6 3-9 5-6s-2 6-5 6zM21 18c6-2 9 3 6 5s-6-2-6-5zM18 21c2 6-3 9-5 6s2-6 5-6zM15 18c-6 2-9-3-6-5s6 2 6 5z" stroke="#1e73be"/></svg></div>
    <h3>Ventilation</h3>
    <p>In publishing and graphic design, Lorem ipsum is a placeholder text commonly used to demonstrate the visual form of a document or a typeface without Lorem ipsum may be used as a before final copy is available.</p>
    <div class="btn btn-outline-blue">Read More</div>
  </article>
  <article class="service-card" style="left:609px">
    <div class="service-icon"><svg width="40" height="30" viewBox="0 0 40 30" fill="none" stroke="#1e73be" stroke-width="1.6"><rect x="2" y="3" width="36" height="13" rx="2"/><line x1="6" y1="12" x2="34" y2="12"/><circle cx="30" cy="7" r="1.2" stroke="#ff8c00"/><path d="M10 20c-2 3-2 5 0 7M20 20v7M30 20c2 3 2 5 0 7" stroke="#ff8c00"/></svg></div>
    <h3>Air conditioning</h3>
    <p>In publishing and graphic design, Lorem ipsum is a placeholder text commonly used to demonstrate the visual form of a document or a typeface without Lorem ipsum may be used as a before final copy is available.</p>
    <div class="btn btn-outline-blue">Read More</div>
  </article>
  <article class="service-card" style="left:832px">
    <div class="service-icon"><svg width="30" height="30" viewBox="0 0 30 30" fill="none" stroke="#1e73be" stroke-width="1.6"><rect x="3" y="3" width="24" height="24" rx="2"/><line x1="8" y1="11" x2="22" y2="11"/><line x1="8" y1="19" x2="22" y2="19"/><rect x="16" y="9" width="3" height="4" fill="#ff8c00" stroke="none"/><rect x="11" y="17" width="3" height="4" fill="#ff8c00" stroke="none"/></svg></div>
    <h3>Installation</h3>
    <p>In publishing and graphic design, Lorem ipsum is a placeholder text commonly used to demonstrate the visual form of a document or a typeface without Lorem ipsum may be used as a before final copy is available.</p>
    <div class="btn btn-outline-blue">Read More</div>
  </article>

  <div class="section-title" style="top:1505px">
    <div class="eyebrow">Our Methods</div>
    <h2>Why choose Choose</h2>
    <div class="rule"></div>
  </div>

  <svg class="abs" style="left:0;top:1444px" width="1200" height="538" viewBox="0 0 1200 538">
    <g fill="none" stroke="#555" stroke-width="1">
      <path d="M477 176H493V221H545"/><path d="M741 176H725V221H673"/>
      <path d="M477 297H519"/><path d="M699 297H741"/>
      <path d="M477 420H493V372H545"/><path d="M741 420H725V372H673"/>
    </g>
    <circle cx="609" cy="297" r="110" fill="#f6f7fa"/>
    <circle cx="609" cy="297" r="90" fill="#fff" stroke="#c9ccd6" stroke-width="1.2"/>
    <circle cx="609" cy="297" r="64" fill="#e4e9f5" role="img" aria-label="Illustration of a technician installing a wall-mounted air conditioner"/>
    <g fill="#1e73be">
      <circle cx="452" cy="176" r="25"/><circle cx="452" cy="297" r="25"/><circle cx="452" cy="420" r="25"/>
      <circle cx="765" cy="176" r="25"/><circle cx="765" cy="297" r="25"/><circle cx="765" cy="420" r="25"/>
    </g>
    <g fill="#fff" stroke="#fff" stroke-width="1.5">
      <circle cx="452" cy="170" r="4"/><circle cx="443" cy="176" r="3"/><circle cx="461" cy="176" r="3"/><rect x="440" y="182" width="24" height="4" rx="2"/>
      <circle cx="450" cy="297" r="11" fill="none"/><path d="M450 290v7h6" fill="none"/>
      <path d="M438 428a14 14 0 0 1 28 -16" fill="none"/>
      <circle cx="765" cy="172" r="9" fill="none" stroke-width="2.5"/><path d="M759 180l-3 10 9-4 9 4-3-10" fill="none"/>
      <circle cx="765" cy="293" r="9" fill="none" stroke-width="2"/><rect x="761" y="302" width="8" height="6" stroke="none"/>
      <path d="M765 408l12 20h-24z" fill="none" stroke-width="2.5"/>
    </g>
    <text x="452" y="425" text-anchor="middle" font-family="Roboto,Arial,sans-serif" font-size="13" font-weight="700" fill="#fff">24</text>
  </svg>

  <div class="why-item why-left" style="top:1594px"><h3>Experienced Team</h3><p>Lorem ipsum dolor sit amet, no utina m tritani omittam qui, mei ob lique tacimates iudicabit.</p></div>
  <div class="why-item why-left" style="top:1716px"><h3>Scheduling at Your Convenience</h3><p>Lorem ipsum dolor sit amet, no utina m tritani omittam qui, mei ob lique tacimates iudicabit.</p></div>
  <div class="why-item why-left" style="top:1839px"><h3>Open 24/7</h3><p>Lorem ipsum dolor sit amet, no utina m tritani omittam qui, mei ob lique tacimates iudicabit.</p></div>
  <div class="why-item why-right" style="top:1594px"><h3>100% Guarantees</h3><p>Lorem ipsum dolor sit amet, no utina m tritani omittam qui, mei ob lique tacimates iudicabit.</p></div>
  <div class="why-item why-right" style="top:1716px"><h3>Cutting Edge Technology</h3><p>Lorem ipsum dolor sit amet, no utina m tritani omittam qui, mei ob lique tacimates iudicabit.</p></div>
  <div class="why-item why-right" style="top:1839px"><h3>We Service All Brands</h3><p>Lorem ipsum dolor sit amet, no utina m tritani omittam qui, mei ob lique tacimates iudicabit.</p></div>

  <section class="financing">
    <div class="abs fin-brand"><span class="dot"></span>LendQuick</div>
    <div class="btn btn-outline-white" style="left:325px;top:71px;width:98px;height:25px;font-size:8.5px">Contact Us</div>
    <div class="abs divider"></div>
    <h2>Customer Financing Options to Help<br>You Achieve Your Indoor Comfort</h2>
  </section>

  <section class="testimonials">
    <div class="eyebrow abs" style="left:188px;top:2173px">Happy Clients</div>
    <h2>Testimonials</h2>
    <div class="btn btn-outline-blue" style="left:188px;top:2232px;width:78px;height:24px;font-size:8.5px">View All</div>
    <div class="btn btn-orange" style="left:273px;top:2232px;width:103px;height:24px;font-size:8.5px">Submit Review</div>
    <div class="abs t-divider"></div>
    <div class="abs t-stars"><i>★★★★★</i>5 of 5</div>
    <div class="abs t-text">In publishing and graphic design, Lorem ipsum is a placeholder text commonly used In publishing and graphic design, Lorem ipsum is a placa typeface without&nbsp; Lorem ipsum may be used as a before final copy is available. to demonstrate the visual form of a document or a typeface without&nbsp; Lorem ipsum may be used as a before final copy is available.</div>
    <div class="abs t-client"><span class="avatar"></span>Client Name</div>
    <svg class="abs" style="left:1013px;top:2180px" width="26" height="56" viewBox="0 0 26 56" fill="none" stroke-width="1.5">
      <circle cx="13" cy="12" r="10" stroke="#ff8c00"/><path d="M18 12H8m4-4-4 4 4 4" stroke="#ff8c00"/>
      <circle cx="13" cy="43" r="10" stroke="#1e73be"/><path d="M8 43h10m-4-4 4 4-4 4" stroke="#1e73be"/>
    </svg>
  </section>

  <div class="abs help-title">Need Help?</div>
  <div class="abs help-call">Call our 24x7x365 Support Team at <b>(718) 555-0147</b></div>

  <section class="connect">
    <h2>Connect With Us</h2>
    <p>Subscribe us to get updates, news &amp; tips in your inbox.</p>
    <div class="abs signup">Get Velmorcorp Email</div>
    <div class="abs signup-btn">SIGN UP</div>
  </section>

  <footer class="site-footer">
    <h2>Easy Access</h2>
    <div class="f-rule" style="top:72px"></div>
    <div class="f-col" style="left:162px">
      <h4>Company</h4>
      <div class="current">About Us</div><div>Why Us</div><div>Our Method</div><div>Testimonial</div><div>Gallery</div><div>FAQ.S</div><div>Meet Our Team</div><div>Terms and Conditions</div><div>Contact Us</div>
    </div>
    <div class="f-col" style="left:317px">
      <h4>Services</h4>
      <div>Cooling Services</div><div class="sub">-&nbsp; Air Conditioning Repair</div><div class="sub">-&nbsp; Air Conditioning Service</div><div class="sub">-&nbsp; Air Conditioning Installation</div>
      <div>Heating Services</div><div class="sub">-&nbsp; Heating Repair</div><div class="sub">-&nbsp; Heating Service</div><div class="sub">-&nbsp; Heating Installation</div>
      <div>Ventilation</div><div>HVAC Maintenance</div>
    </div>
    <div class="f-col" style="left:507px">
      <h4>Working Hours</h4>
      <table>
        <tr><td>Monday</td><td>8:00AM TO 5:00PM</td></tr>
        <tr><td>Tuesday</td><td>8:00AM TO 5:00PM</td></tr>
        <tr><td>Wednesday</td><td>00AM TO 5:00PM</td></tr>
        <tr><td>Thursday</td><td>8:00AM TO 5:00PM</td></tr>
        <tr><td>Friday</td><td>8:00AM TO 5:00PM</td></tr>
        <tr><td>Saturday</td><td>Closed</td></tr>
        <tr><td>Sunday</td><td>Closed</td></tr>
      </table>
    </div>
    <div class="f-col" style="left:696px">
      <h4>Location</h4>
      <div class="f-loc">Velmor Mechanical Contractors</div>
      <div class="f-loc">Brooklyn, NY 11200</div>
      <div class="f-loc" style="margin-top:4px"><span class="lbl">Phone:</span> (718) 555-0147</div>
      <div class="f-loc" style="margin-top:4px"><span class="lbl">Email:</span> info@velmorcorp.example</div>
      <div style="margin-top:14px">More of Us</div>
    </div>
    <div class="f-col" style="left:893px"><h4>We Accept</h4></div>
  </footer>

  <div class="pay" style="left:893px;top:2596px;background:#e8eaf0"></div>
  <div class="pay" style="left:922px;top:2596px;background:#f4f5f8"></div>
  <div class="pay" style="left:951px;top:2596px;background:#e0e6f2"></div>
  <div class="pay" style="left:980px;top:2596px;background:#5b8bd0"></div>
  <div class="pay" style="left:893px;top:2615px;background:#f4f5f8"></div>
  <div class="pay" style="left:922px;top:2615px;background:#e8eaf0"></div>
  <div class="pay" style="left:951px;top:2615px;background:#f4f5f8"></div>

  <div class="social" style="left:697px;background:var(--blue)"></div>
  <div class="social" style="left:725px;background:var(--orange)"></div>
  <div class="social" style="left:754px;background:var(--blue)"></div>
  <div class="social" style="left:781px;background:var(--blue)"></div>

  <div class="f-rule" style="top:2804px"></div>
  <div class="abs copyright">Copyright © 2021 <span>Velmorcorp</span>. All rights reserved&nbsp; |&nbsp; Privacy &amp; Policy</div>

</div>
</body>
</html>
```